Looking for a website that shows the services available to customers.This company will provide consulting on how to reduce costs and improve overal IT spend within any organization. We will employ experts in many aspects of IT including Cloud, Mainframe, AS400/iSeries/PSeries, Disaster Recovery, IT optimization strategies, Colocation, Hybrid IT, Migrations, Networking, Security etc. I am a technology advisor that helps to optimize costs in IT

Target Market(s)

Al companies over $1M in revenue

Industry/Entity Type

It Company

Number of Pages Required

5+ page

Font styles to use
Serif
Sans Serif

Requirements
Must have
• Tabs for: About us (our team), Services, Why Norvale, Testimonials, Contact Us
Nice to have
• i would like to have on my services pages some logos of partners. Such as quillbrook, D&K, etc.

I need an understanding of how to add/change to the website
Should not have
• no spirlay fonts or any thing scrolly. I want t professional IT website

```html
<!DOCTYPE html>
<html lang="en">
<head>
<meta charset="utf-8">
<title>Norvale — IT Cost Advisory</title>
<link href="https://fonts.googleapis.com/css2?family=Exo+2:ital,wght@0,500;0,600;0,700;0,800;0,900;1,700&family=Open+Sans:wght@400;600;700&display=swap" rel="stylesheet">
<style>
:root{
  --green:#8dc63f;
  --teal:#2bb5a0;
  --navy:#2a3a8c;
  --blue-band:#2185c0;
  --link-blue:#1f5fa6;
  --purple:#9b3fb5;
  --ink:#111418;
  --body:#5b5f66;
  --soft:#f1f2f6;
  --footer:#16191c;
  --white:#ffffff;
  --star:#f7931e;
}
*{box-sizing:border-box;margin:0;padding:0}
html,body{width:1200px;height:3622px;overflow:hidden;background:var(--white)}
body{position:relative;font-family:"Open Sans",sans-serif;color:var(--body)}
.abs{position:absolute}
.heading{font-family:"Exo 2",sans-serif;color:var(--ink);font-weight:700}
.btn{position:absolute;display:flex;align-items:center;justify-content:center;color:var(--white);font-family:"Exo 2",sans-serif;font-weight:600;font-size:14px;letter-spacing:.2px;background:linear-gradient(90deg,var(--teal),#3cb58c)}
.wordmark{font-family:"Exo 2",sans-serif;font-weight:600;display:flex;align-items:center;gap:8px}
.wordmark .dot{width:14px;height:14px;border-radius:50%;background:var(--green)}

/* header */
.site-header{position:absolute;left:0;top:0;width:1200px;height:92px;background:var(--white)}
.site-header .wordmark{position:absolute;left:162px;top:44px;font-size:30px;color:var(--ink)}
.phone{position:absolute;left:902px;top:10px;font-family:"Exo 2",sans-serif;font-weight:600;font-size:17px;color:var(--ink);display:flex;align-items:center;gap:6px}
.main-nav{position:absolute;left:487px;top:54px;display:flex;gap:25px;font-size:12.5px;color:#2b2f36}
.main-nav .active{color:var(--green);position:relative}
.main-nav .active::after{content:"";position:absolute;left:-4px;right:-4px;top:30px;height:3px;background:var(--green)}
.header-cta{left:903px;top:44px;width:135px;height:37px;font-size:17px;font-weight:500}

/* hero */
.hero{position:absolute;left:0;top:92px;width:1200px;height:662px}
.hero-photo{position:absolute;inset:0;background:radial-gradient(ellipse at 30% 35%,#4a4d4f 0%,#2c2f31 45%,#15181a 100%)}
.hero-title{position:absolute;right:159px;top:158px;text-align:right;font-family:"Exo 2",sans-serif;line-height:1}
.hero-title .lead{display:block;color:var(--green);font-weight:600;font-size:50px}
.hero-title .big{display:block;color:var(--white);font-weight:900;font-size:62px;margin-top:6px;letter-spacing:1px}
.hero-copy{position:absolute;right:159px;top:284px;width:400px;text-align:right;color:#e8e8e8;font-size:14px;line-height:23px}
.hero-cta{left:903px;top:348px;width:135px;height:40px}
.hero-arrow{position:absolute;top:243px}

/* welcome */
.welcome-kicker{left:294px;top:831px;font-size:14px;color:var(--purple)}
.welcome-title{left:290px;top:852px;font-size:42px}
.welcome-lead{left:290px;top:917px;width:290px;font-size:12.5px;line-height:21px;color:var(--link-blue)}
.welcome-body{left:290px;top:995px;width:300px;font-size:11.5px;line-height:21px}
.welcome-cta{left:293px;top:1093px;width:135px;height:40px}
.welcome-block{left:723px;top:957px;width:110px;height:157px;background:var(--navy)}
.welcome-photo{left:813px;top:817px;width:214px;height:207px;background:radial-gradient(circle at 55% 45%,#6fa0d6,#1b3a6b 60%,#0c1a35)}
.welcome-figure{left:700px;top:830px;width:200px;height:284px;background:linear-gradient(180deg,#d9c2ad,#f2f2f2 45%,#e6e6e6);border-radius:90px 90px 10px 10px}

/* services */
.section-title{position:absolute;left:0;width:1200px;text-align:center;font-family:"Exo 2",sans-serif;font-weight:700;color:var(--ink)}
.section-sub{position:absolute;left:0;width:1200px;text-align:center;font-size:12.5px;line-height:22px}
.service-band{left:0;top:1490px;width:1200px;height:392px}
.service-card{position:absolute;top:1335px;width:246px;height:405px;background:var(--white);text-align:center}
.service-card .media{height:210px}
.service-card h3{font-family:"Exo 2",sans-serif;font-weight:600;font-size:17px;color:var(--ink);margin-top:28px}
.service-card p{font-size:12px;line-height:22.5px;padding:0 20px;margin-top:10px}
.service-card .more{display:inline-flex;align-items:center;gap:10px;margin-top:12px;font-family:"Exo 2",sans-serif;font-weight:700;font-size:12.5px;color:var(--navy)}
.go{width:20px;height:20px;border-radius:50%;background:var(--teal);display:inline-flex;align-items:center;justify-content:center}
.services-cta{left:509px;top:1763px;width:180px;height:41px;background:linear-gradient(90deg,var(--teal),var(--green))}

/* testimonials */
.stars{right:722px;top:1980px;display:flex;gap:6px}
.quote-short{right:722px;top:2024px;width:260px;text-align:right;font-size:13.5px;line-height:24px}
.read-more{right:722px;top:2113px;display:flex;align-items:center;gap:13px;font-family:"Exo 2",sans-serif;font-weight:700;font-size:12px;color:var(--navy)}
.divider{left:523px;top:1963px;width:1px;height:200px;background:#e1e3e8}
.quote-big{left:580px;top:1985px;width:420px;font-family:"Exo 2",sans-serif;font-style:italic;font-weight:700;font-size:22px;line-height:32px;color:#2b2f36}
.avatar{left:578px;top:2075px;width:68px;height:68px;border-radius:50%;background:linear-gradient(160deg,#a8886c,#3f3530)}
.client{left:660px;top:2090px;font-family:"Exo 2",sans-serif;font-size:16px;color:var(--green)}
.client::before{content:"– ";color:var(--ink)}
.client small{display:block;font-family:"Open Sans",sans-serif;font-size:10.5px;color:var(--body);margin-left:19px}

/* why */
.why-panel{left:412px;top:2240px;width:788px;height:464px;background:var(--soft)}
.why-photo{left:285px;top:2345px;width:254px;height:254px;border-radius:50%;background:linear-gradient(135deg,#d8dde4,#7d8896 50%,#2c3a55)}
.why-title{left:633px;top:2307px;font-size:36px}
.why-copy{left:636px;top:2363px;width:350px;font-size:12px;line-height:22.5px}
.why-list{left:639px;top:2451px;list-style:none;font-size:12px;color:#2b2f36}
.why-list li{display:flex;align-items:center;gap:14px;height:33.5px}
.why-cta{left:639px;top:2589px;width:135px;height:40px}

/* experts */
.expert{position:absolute;top:2915px;width:201px;height:203px}
.expert-tag{left:400px;top:3042px;width:178px;height:76px;background:linear-gradient(90deg,rgba(43,181,160,.92),rgba(141,198,63,.92));color:var(--white);text-align:center;padding-top:14px}
.expert-tag b{display:block;font-family:"Exo 2",sans-serif;font-weight:600;font-size:17px}
.expert-tag span{font-size:11px}

/* cta band */
.question{left:0;top:3197px;width:1200px;height:119px;background:linear-gradient(90deg,#2bb5a0,#8dc63f)}
.question h2{position:absolute;left:344px;top:40px;font-family:"Exo 2",sans-serif;font-weight:600;font-size:30px;color:var(--white)}
.question .outline{left:723px;top:39px;width:135px;height:41px;background:none;border:1px solid var(--white)}

/* footer */
.site-footer{left:0;top:3316px;width:1200px;height:306px;background:linear-gradient(180deg,#1d2124,#101214);color:#b9bcc0}
.foot-head{position:absolute;top:46px;font-family:"Exo 2",sans-serif;font-weight:600;font-size:15px;color:var(--white)}
.sitemap{position:absolute;left:163px;top:88px;list-style:none;font-size:11px}
.sitemap li{height:23.2px;display:flex;align-items:center;gap:12px}
.sitemap li::before{content:"";width:5px;height:5px;background:var(--green)}
.foot-mark{left:0;width:1200px;top:120px;justify-content:center;font-size:44px;color:var(--white)}
.socials{left:545px;top:182px;display:flex;gap:2px}
.socials span{width:34px;height:34px;border-radius:50%;background:#2a63c9;border:2px solid #3d7be0}
.copyright{left:0;width:1200px;top:238px;text-align:center;font-size:10px;color:#cfd2d6}
.copyright em{font-style:normal;color:var(--green)}
.contact{position:absolute;right:200px;text-align:right;font-size:11px;line-height:17px}
.contact-icon{position:absolute;left:1021px}
</style>
</head>
<body>

<header class="site-header">
  <div class="wordmark"><span class="dot"></span>Norvale</div>
  <div class="phone">
    <svg width="16" height="16" viewBox="0 0 24 24"><path fill="#8dc63f" d="M6.6 10.8c1.4 2.8 3.8 5.1 6.6 6.6l2.2-2.2c.3-.3.7-.4 1-.2 1.1.4 2.3.6 3.6.6.6 0 1 .4 1 1V20c0 .6-.4 1-1 1C10.6 21 3 13.4 3 4c0-.6.4-1 1-1h3.5c.6 0 1 .4 1 1 0 1.3.2 2.5.6 3.6.1.3 0 .7-.2 1z"/></svg>
    123 456 7890
  </div>
  <nav class="main-nav">
    <span class="active">Home</span><span>About Us</span><span>Services</span><span>Why Norvale</span><span>Testimonials</span>
  </nav>
  <div class="btn header-cta">Contact Us</div>
</header>

<section class="hero">
  <div class="hero-photo" role="img" aria-label="Bearded professional working at a computer in a dim office"></div>
  <svg class="hero-arrow" style="left:70px" width="20" height="36" viewBox="0 0 20 36"><path d="M18 2 2 18l16 16" fill="none" stroke="#999" stroke-width="2"/></svg>
  <svg class="hero-arrow" style="left:1110px" width="20" height="36" viewBox="0 0 20 36"><path d="M2 2l16 16L2 34" fill="none" stroke="#fff" stroke-width="2"/></svg>
  <h1 class="hero-title"><span class="lead">LEAD WITH</span><span class="big">CONFIDENCE</span></h1>
  <p class="hero-copy">Lorem Ipsum is simply dummy text of the printing and typesetting industry Lorem Ipsum has.</p>
  <div class="btn hero-cta">CONTACT US</div>
  <svg class="abs" style="left:0;top:540px" width="1200" height="122" viewBox="0 0 1200 122">
    <polygon points="0,82 160,118 300,122 560,94 900,46 1020,82 1200,28 1200,122 0,122" fill="#fff"/>
    <polygon points="160,118 225,131 268,116" fill="#8dc63f"/>
    <polygon points="560,94 900,46 760,100" fill="#2a83c2"/>
    <polygon points="900,46 1020,82 955,82" fill="#6a3fb0"/>
    <polygon points="1020,82 1200,28 1200,46" fill="#2a6fc0"/>
  </svg>
</section>

<p class="abs welcome-kicker">Welcome To</p>
<h2 class="abs heading welcome-title">Norvale</h2>
<p class="abs welcome-lead">Lorem Ipsum is simply dummy text of the Text printing and typesetting industry. Lorem Ipsum has been the industry's text print.</p>
<p class="abs welcome-body">Lorem Ipsum is simply dummy text of the printing and typesetting industry. Lorem Ipsum has been the industry's standard dummy text ever since the 1500s, when an unknown printer.</p>
<div class="btn welcome-cta">LEARN MORE</div>
<div class="abs welcome-block"></div>
<div class="abs welcome-photo" role="img" aria-label="Glowing digital network background"></div>
<div class="abs welcome-figure" role="img" aria-label="Smiling man in white shirt holding a tablet"></div>

<h2 class="section-title" style="top:1205px;font-size:36px">Services We Provide</h2>
<p class="section-sub" style="top:1261px">Lorem Ipsum is simply dummy text of the printing and typesetting industry<br>Lorem Ipsum has been the industry.</p>

<svg class="abs service-band" viewBox="0 0 1200 392" width="1200" height="392">
  <defs><linearGradient id="bandFill" x1="0" y1="0" x2="1" y2="1"><stop offset="0" stop-color="#2190c6"/><stop offset=".6" stop-color="#2a4f9e"/><stop offset="1" stop-color="#2b3690"/></linearGradient></defs>
  <polygon points="0,12 560,48 1200,0 1200,392 0,392" fill="url(#bandFill)"/>
</svg>

<article class="service-card" style="left:207px">
  <div class="media" role="img" aria-label="Night city skyline with cloud connections" style="background:linear-gradient(180deg,#6f8fb8,#1d3157 70%,#0d1a30)"></div>
  <h3>Cloud</h3>
  <p>Lorem Ipsum is simply dummy text of the printing and typesetting the industry has been</p>
  <span class="more">Learn More <span class="go"><svg width="9" height="9" viewBox="0 0 10 10"><path d="M3 1l4 4-4 4" fill="none" stroke="#fff" stroke-width="1.8"/></svg></span></span>
</article>
<article class="service-card" style="left:477px">
  <div class="media" role="img" aria-label="Rows of server racks in a data centre" style="background:linear-gradient(180deg,#e9eef1,#4b5560 45%,#c9d0d4)"></div>
  <h3>Mainframe</h3>
  <p>Lorem Ipsum is simply dummy text of the printing and typesetting the industry has been</p>
  <span class="more">Learn More <span class="go"><svg width="9" height="9" viewBox="0 0 10 10"><path d="M3 1l4 4-4 4" fill="none" stroke="#fff" stroke-width="1.8"/></svg></span></span>
</article>
<article class="service-card" style="left:747px">
  <div class="media" role="img" aria-label="Hand touching a network of connected people icons" style="background:linear-gradient(135deg,#2a5f8f,#0f2c4d 60%,#1a4e7c)"></div>
  <h3>Networking</h3>
  <p>Lorem Ipsum is simply dummy text of the printing and typesetting the industry has been</p>
  <span class="more">Learn More <span class="go"><svg width="9" height="9" viewBox="0 0 10 10"><path d="M3 1l4 4-4 4" fill="none" stroke="#fff" stroke-width="1.8"/></svg></span></span>
</article>
<div class="btn services-cta">VIEW ALL SERVICES</div>

<div class="abs stars">
  <svg width="138" height="22" viewBox="0 0 138 22"><g fill="#f7931e">
    <path id="st" d="M11 1l3 6.6 7.2.8-5.4 4.9 1.5 7.1L11 16.8l-6.3 3.6 1.5-7.1L.8 8.4 8 7.6z"/>
    <use href="#st" x="29"/><use href="#st" x="58"/><use href="#st" x="87"/><use href="#st" x="116"/></g></svg>
</div>
<p class="abs quote-short">"Lorem Ipsum is simply dummy text of the printing and type Lorem Ipsum has been the industry's&nbsp;&nbsp;"</p>
<div class="abs read-more">Read More Testimonials <span class="go" style="width:24px;height:24px"><svg width="10" height="10" viewBox="0 0 10 10"><path d="M3 1l4 4-4 4" fill="none" stroke="#fff" stroke-width="1.8"/></svg></span></div>
<div class="abs divider"></div>
<p class="abs quote-big">" Lorem Ipsum is simply dummy text of the printing type"</p>
<div class="abs avatar" role="img" aria-label="Client portrait"></div>
<p class="abs client">Client Name<small>Something.com</small></p>

<div class="abs why-panel"></div>
<div class="abs why-photo" role="img" aria-label="Two businessmen reviewing a laptop together"></div>
<h2 class="abs heading why-title">Why Norvale</h2>
<p class="abs why-copy">Lorem Ipsum is simply dummy text of the printing and typesetting industry Lorem Ipsum has been the industry's standard dummy text ever since the.</p>
<ul class="abs why-list">
  <li><span class="go" style="width:18px;height:18px"><svg width="8" height="8" viewBox="0 0 10 10"><path d="M3 1l4 4-4 4" fill="none" stroke="#fff" stroke-width="2"/></svg></span>Lorem Ipsum is simply dummy text</li>
  <li><span class="go" style="width:18px;height:18px"><svg width="8" height="8" viewBox="0 0 10 10"><path d="M3 1l4 4-4 4" fill="none" stroke="#fff" stroke-width="2"/></svg></span>Lorem Ipsum is text printy type industry</li>
  <li><span class="go" style="width:18px;height:18px"><svg width="8" height="8" viewBox="0 0 10 10"><path d="M3 1l4 4-4 4" fill="none" stroke="#fff" stroke-width="2"/></svg></span>Lorem Ipsum is simply text unknown printer</li>
  <li><span class="go" style="width:18px;height:18px"><svg width="8" height="8" viewBox="0 0 10 10"><path d="M3 1l4 4-4 4" fill="none" stroke="#fff" stroke-width="2"/></svg></span>Lorem Ipsum is simply dummy text</li>
</ul>
<div class="btn why-cta">LEARN MORE</div>

<h2 class="section-title" style="top:2782px;font-size:36px">Meet Our Experts</h2>
<p class="section-sub" style="top:2838px">Lorem Ipsum is simply dummy text of the Text printing and typesetting<br>industry. Lorem Ipsum has been the industry's text print.</p>
<div class="expert" style="left:162px;background:linear-gradient(180deg,#dcdcdc,#b9b9b9 55%,#2a3550)" role="img" aria-label="Expert in navy suit holding a coffee cup"></div>
<div class="expert" style="left:387px;background:linear-gradient(180deg,#b9c3cc,#e8e4df 60%,#f4f4f4)" role="img" aria-label="Expert in white blouse"></div>
<div class="expert" style="left:612px;background:linear-gradient(180deg,#d2d2d2,#a8a8a8 50%,#3c3d40)" role="img" aria-label="Expert in grey suit holding a phone"></div>
<div class="expert" style="left:837px;background:linear-gradient(180deg,#b9c3cc,#e8e4df 60%,#f4f4f4)" role="img" aria-label="Expert with arms crossed in white blouse"></div>
<div class="abs expert-tag"><b>Client Name</b><span>Something.com</span></div>

<section class="abs question">
  <h2>Have An Any Question ?</h2>
  <div class="btn outline">CONTACT US</div>
</section>

<footer class="abs site-footer">
  <h4 class="foot-head" style="left:163px">Sitemap</h4>
  <ul class="sitemap">
    <li>Home</li><li>About us</li><li>Services</li><li>Why Norvale</li><li>Testimonials</li><li>Contact Us</li>
  </ul>
  <div class="abs wordmark foot-mark"><span class="dot"></span>Norvale</div>
  <div class="abs socials" aria-label="Social links"><span></span><span></span><span></span></div>
  <p class="abs copyright"><em>©Norvale</em> – 2020 All Rights reserved.</p>

  <h4 class="foot-head" style="right:164px">Contact Us</h4>
  <p class="contact" style="top:90px;color:#fff;font-family:'Exo 2',sans-serif;font-size:13px;font-weight:600">Norvale</p>
  <p class="contact" style="top:113px">101 - Lorem ipsum simple text<br>print type text industry.</p>
  <p class="contact" style="top:162px;font-size:14px;color:#fff">+(1) 123 456 7890</p>
  <p class="contact" style="top:198px">info@norvaleadvisory.com</p>
  <svg class="contact-icon" style="top:89px" width="18" height="22" viewBox="0 0 18 22"><path d="M9 1a7 7 0 0 0-7 7c0 5 7 12 7 12s7-7 7-12a7 7 0 0 0-7-7z" fill="none" stroke="#8dc63f" stroke-width="1.8"/><circle cx="9" cy="8" r="2.5" fill="#8dc63f"/></svg>
  <svg class="contact-icon" style="top:162px" width="17" height="17" viewBox="0 0 24 24"><path fill="#8dc63f" d="M6.6 10.8c1.4 2.8 3.8 5.1 6.6 6.6l2.2-2.2c.3-.3.7-.4 1-.2 1.1.4 2.3.6 3.6.6.6 0 1 .4 1 1V20c0 .6-.4 1-1 1C10.6 21 3 13.4 3 4c0-.6.4-1 1-1h3.5c.6 0 1 .4 1 1 0 1.3.2 2.5.6 3.6.1.3 0 .7-.2 1z"/></svg>
  <svg class="contact-icon" style="top:199px" width="17" height="13" viewBox="0 0 17 13"><rect width="17" height="13" rx="1.5" fill="#8dc63f"/><path d="M1 1.5l7.5 6 7.5-6" fill="none" stroke="#16191c" stroke-width="1.4"/></svg>
</footer>

</body>
</html>
```